Website for Torvik Capital

We need a new web design for a company based in Chicago called "Torvik Capital". TVK provides portfolio management and financial advice using primarily income oriented strategies, such as, dividend paying stocks and preferred stocks. Our niche is utilizing conservative option strategies to help generate income and minimize risk. We are looking for a clean-cut and streamline professional site that is both appealing and user friendly. We would like the main colors to be the dark blue and bright green of our logo. Depending on cost and ease, we may want a designer to give us the completed website, including the coding, etc.

Target Market(s)

20-80 year old affluent investors seeking portfolio management and investment advice.

Industry/Entity Type

Conservative

Requirements
Must have
• -our logo
-main tabs: home, about us, our philosophy, our services, investment strategy, compliance, contact us
-our phone number visible and conveniently placed on each page
Nice to have
• -conveniently placed login button for current clients
-conveniently placed "quick contact" box on home page with spaces for first name, last name, email, phone number, and a blank box for their question or comment
-check us out on Facebook and Twitter logos/buttons
-we like the idea of rotating pictures on top of page, but we aren't sure whether or not we definitely want that
Should not have
• -no trees
-no clocks
-no timers
-no crowns
-no plants

```html
<!DOCTYPE html>
<html lang="en">
<head>
<meta charset="utf-8">
<title>Torvik Capital</title>
<link href="https://fonts.googleapis.com/css2?family=PT+Sans:ital,wght@0,400;0,700;1,400;1,700&family=Libre+Baskerville:ital@0;1&display=swap" rel="stylesheet">
<style>
:root{
  --navy:#0b0f6e;
  --green:#8cc63f;
  --green-dark:#5f9e12;
  --bar:#5b5b5b;
  --footer:#575757;
  --text:#555;
  --line:#dcdcdc;
  --field:#ececec;
}
*{margin:0;padding:0;box-sizing:border-box}
html,body{width:960px;height:1200px;overflow:hidden}
body{position:relative;background:#fff;font-family:"PT Sans",sans-serif;color:var(--text)}
.abs{position:absolute}

/* top bar */
.top-bar{left:0;top:0;width:960px;height:28px;background:var(--bar)}
.util-links{left:600px;top:8px;font-size:9px;color:#ddd}
.util-links span{margin:0 5px;color:#aaa}
.client-login{left:744px;top:0;width:112px;height:28px;background:var(--green);color:#fff;font-size:11px;font-weight:700;display:flex;align-items:center;justify-content:center;gap:6px}

/* header */
.site-header{left:0;top:28px;width:960px;height:98px;background:linear-gradient(#f7f7f7,#ececec);border-bottom:1px solid #d4d4d4}
.brand{left:110px;top:38px;display:flex;align-items:center;gap:10px}
.brand-mark{width:40px;height:40px;background:var(--navy)}
.brand-name{font-size:22px;font-weight:700;color:var(--navy);letter-spacing:3px}
.call-icon{left:660px;top:60px}
.call-label{left:700px;top:56px;font-size:15px;color:#555}
.call-number{left:700px;top:72px;font-family:"Libre Baskerville",serif;font-size:21px;color:var(--navy)}

/* nav */
.main-nav{left:104px;top:132px;width:752px;height:52px;background:var(--green);border:1px solid #79b22e;display:flex}
.main-nav a{display:flex;align-items:center;padding:0 18px;font-size:10.5px;font-weight:700;color:#fff;text-decoration:none;text-shadow:0 1px 1px rgba(0,0,0,.35);border-right:1px solid #a3d266}
.main-nav a:last-child{border-right:0;flex:1;justify-content:center}
.main-nav a.active{color:var(--navy);text-shadow:none}

/* slider */
.slider{left:104px;top:186px;width:752px;height:338px;background:#fff;border:1px solid #e2e2e2;box-shadow:0 10px 10px -8px rgba(0,0,0,.3)}
.slide-photo{left:3px;top:3px;width:744px;height:330px;background:linear-gradient(100deg,#e3e7ec 0%,#c9cfd8 35%,#dfe3e8 55%,#3b4a6a 100%)}
.slider-dots{left:26px;top:296px;display:flex;gap:7px}
.slider-dots i{width:20px;height:20px;border-radius:50%;background:rgba(235,235,235,.7)}
.slider-dots i:first-child{background:#fff;box-shadow:0 0 0 2px #bbb}
.rule{height:1px;background:linear-gradient(90deg,transparent,var(--line) 15%,var(--line) 85%,transparent)}

h2{font-weight:400;font-size:19px;color:var(--navy)}
h3{font-size:12.5px;font-weight:700;color:var(--green-dark)}
p{font-size:10px;line-height:18.4px}

.intro{font-style:italic;font-weight:700;color:var(--green-dark);font-size:10.5px;line-height:16px;margin:8px 0 3px}
.btn-light{display:inline-block;background:linear-gradient(#f0f0f0,#dcdcdc);border:1px solid #d0d0d0;color:var(--navy);font-size:11px;padding:6px 9px}
.thumb{width:157px;height:82px;border:1px solid #ddd;padding:2px;background:#fff}
.thumb div{width:100%;height:100%}
.vrule{width:1px;background:var(--line)}

.date-badge{width:73px;height:66px;background:linear-gradient(#fff,#ececec);border:1px solid #ddd;box-shadow:0 4px 4px -2px rgba(0,0,0,.25);text-align:center;font-family:"Libre Baskerville",serif;font-style:italic}
.date-badge .m{display:block;font-size:17px;color:#666;margin-top:6px}
.date-badge .d{display:block;font-size:26px;color:var(--green-dark);line-height:26px}
.read-more{font-style:italic;color:var(--navy);font-size:8.5px}

.contact-box{left:494px;top:908px;width:362px;height:202px;background:#f4f4f4;border:2px solid #e0e0e0}
.field{position:absolute;background:var(--field);border:1px solid #d6d6d6;font-size:9.5px;color:#888;padding:6px 7px}
.btn{position:absolute;top:162px;width:72px;height:27px;display:flex;align-items:center;justify-content:center;color:#fff;font-size:11px}

.site-footer{left:0;top:1124px;width:960px;height:76px;background:var(--footer)}
.copyright{left:105px;top:35px;font-size:9.5px;color:#ddd}
.social{left:737px;top:25px;display:flex;gap:7px}
.social i{width:25px;height:25px;border-radius:3px;background:#8d8d8d}
</style>
</head>
<body>

<div class="abs top-bar"></div>
<div class="abs util-links">FAQ<span>|</span>Blog<span>|</span>Site Map</div>
<div class="abs client-login">
  <svg width="12" height="12" viewBox="0 0 12 12"><circle cx="6" cy="3.5" r="3" fill="#fff"/><path d="M0 12c0-4 3-5 6-5s6 1 6 5z" fill="#fff"/></svg>
  CLIENT LOGIN
</div>

<header class="abs site-header"></header>
<div class="abs brand"><span class="brand-mark"></span><span class="brand-name">TORVIK CAPITAL</span></div>
<svg class="abs call-icon" width="32" height="36" viewBox="0 0 32 36"><path d="M6 2c-3 2-5 6-2 14s9 14 14 16c3 1 6 0 8-3l-5-6-4 3c-3-1-7-7-8-11l4-3z" fill="#c8161d"/><ellipse cx="18" cy="33" rx="12" ry="2" fill="rgba(0,0,0,.15)"/></svg>
<div class="abs call-label">Call Us:</div>
<div class="abs call-number">+180 555 0142</div>

<nav class="abs main-nav">
  <a class="active" href="#">HOME</a>
  <a href="#">ABOUT US</a>
  <a href="#">OUR PHILOSOPHY</a>
  <a href="#">OUR SERVICES</a>
  <a href="#">INVESTMENT STRATEGY</a>
  <a href="#">COMPLIANCE</a>
  <a href="#">CONTACT US</a>
</nav>

<section class="abs slider">
  <div class="abs slide-photo" role="img" aria-label="Photo of an advisor shaking hands with a smiling couple in a bright office"></div>
  <div class="abs slider-dots"><i></i><i></i><i></i><i></i></div>
</section>

<div class="abs rule" style="left:104px;top:552px;width:752px"></div>

<section class="abs about" style="left:104px;top:570px;width:240px">
  <h2>About Our Company</h2>
  <p class="intro">Lorem ipsum dolor sit amet, consectetur adipi-scing elit. Fusce accumsan, elit a suscipit sagittis, tortor sapien cursus risus, non rhoncus lectus nunc ac nulla...</p>
  <p>Aliquam molestie, mi et imperdiet euismod, dui purus auctor tellus, et interdum lacus lectus et ante. Sed accumsan sollicitudin sapien, sit amet adipi-scing turpis gravida ac. In congue, neque ac lobortis volutpat, libero mauris varius mi, vitae suscipit ipsum ligula vitae risus.</p>
  <span class="btn-light" style="margin-top:18px">Read More</span>
</section>
<div class="abs vrule" style="left:360px;top:572px;height:248px"></div>

<section class="abs services" style="left:378px;top:570px;width:478px">
  <h2>What We Do</h2>
</section>
<div class="abs thumb" style="left:378px;top:604px"><div role="img" aria-label="Photo of hands reviewing financial charts on a desk" style="background:linear-gradient(135deg,#d7dbe0,#8e9299)"></div></div>
<div class="abs" style="left:552px;top:602px;width:300px">
  <h3>Portfolio Management</h3>
  <p style="margin-top:3px">Sed accumsan sollicitudin sapien, sit amet adipiscing turpis gravida ac. In congue, neque ac lobortis volutpat, libero mauris varius mi, vitae suscipit ipsum ligula vitae risus.</p>
</div>
<div class="abs" style="left:378px;top:706px;width:478px;height:1px;background:var(--line)"></div>
<div class="abs thumb" style="left:378px;top:726px"><div role="img" aria-label="Photo of an advisor meeting with a couple" style="background:linear-gradient(135deg,#e6e9ec,#9aa4b2)"></div></div>
<div class="abs" style="left:552px;top:724px;width:300px">
  <h3>Financial Advising</h3>
  <p style="margin-top:3px">Sed accumsan sollicitudin sapien, sit amet adipiscing turpis gravida ac. In congue, neque ac lobortis volutpat, libero mauris varius mi, vitae suscipit ipsum ligula vitae risus.</p>
</div>

<div class="abs rule" style="left:104px;top:848px;width:752px"></div>

<section class="abs news" style="left:104px;top:869px;width:360px">
  <h2>Latest News</h2>
</section>
<div class="abs date-badge" style="left:104px;top:908px"><span class="m">Apr</span><span class="d">01</span></div>
<div class="abs" style="left:201px;top:906px;width:250px">
  <h3>Heading Goes Here</h3>
  <p style="margin-top:2px">Sed accumsan sollicitudin sapien, sit amet adipiscing turpis gravida ac. In congue, neque ac lobortis volut-pat, libero mauris varius mi.. <span class="read-more">Read More</span></p>
</div>
<div class="abs date-badge" style="left:104px;top:1008px"><span class="m">Mar</span><span class="d">30</span></div>
<div class="abs" style="left:201px;top:1006px;width:250px">
  <h3>Heading Goes Here</h3>
  <p style="margin-top:2px">Sed accumsan sollicitudin sapien, sit amet adipiscing turpis gravida ac. In congue, neque ac lobortis volut-pat, libero mauris varius mi.. <span class="read-more">Read More</span></p>
</div>
<div class="abs vrule" style="left:472px;top:874px;height:230px"></div>

<h2 class="abs" style="left:494px;top:869px">Quick Contact</h2>
<form class="abs contact-box">
  <div class="field" style="left:12px;top:20px;width:159px;height:23px">First Name</div>
  <div class="field" style="left:183px;top:20px;width:159px;height:23px">Last Name</div>
  <div class="field" style="left:12px;top:56px;width:159px;height:23px">Email Address</div>
  <div class="field" style="left:183px;top:56px;width:159px;height:23px">Phone No.</div>
  <div class="field" style="left:12px;top:92px;width:330px;height:60px">Comments</div>
  <div class="btn" style="left:184px;background:#555">CLEAR</div>
  <div class="btn" style="left:270px;background:var(--green)">SUBMIT</div>
</form>

<footer class="abs site-footer">
  <div class="abs copyright">Copyright © 2013. <b>Torvik Capital.</b> All Right Reserved</div>
  <div class="abs social" aria-label="Social links"><i></i><i></i><i></i><i></i></div>
</footer>

</body>
</html>
```